Bright Leaf Bistro & Pantry Squarespace Website Files

We need a Squarespace website for a new company called "Bright Leaf Bistro & Pantry".

The company is committed to providing the highest quality, fresh and natural food, health and wellness products.

We would like to see designs that use the colors of our logo. Please provide graphic design and layout for the site.

The final design should communicate health and wellness.

Target Market(s)

Bright Leaf Bistro & Pantry is a new company that will offer customers organic and
locally grown produce, chemical and preservative-free groceries, cruelty-free body care and eco-household products. Additionally, our kitchen will offer healthy lunch and dinner options emphasizing organic and whole food options, recognizing the trend within the restaurant industry for the demand for healthy cuisine. The restaurant will procure local foods when possible, reducing dependence on fossil fuels used for transportation. All of our products are healthy alternatives to the products available at conventional grocery chains.

Located in the heart of the growing Harlow Street section of Lewiston, NY, the
marketplace will serve a community of residents in Lewiston, residents in
Niagara Falls, and residents in Niagara Falls, Ontario, Canada.

The creation of the marketplace is in response to the growing demand in the community for a local natural food store.

Industry/Entity Type

Cafe

Font styles to use
Sans Serif

Colors
00a990
faa54b
87cfc7
f37122

Requirements
Must have
• Home page, Events, Cafe Menu, Marketplace Products, Health Info, News, Recipes, Contact Us (Email form and Social Media links), Newsletter sign up.
Nice to have
• Order Online
Should not have
• (Can't think of anything right now :-)

```html
<!DOCTYPE html>
<html lang="en">
<head>
<meta charset="utf-8">
<title>Bright Leaf Bistro &amp; Pantry</title>
<link href="https://fonts.googleapis.com/css2?family=Jost:ital,wght@0,400;0,500;0,600;1,500&family=Lato:ital,wght@0,400;0,700;1,400&display=swap" rel="stylesheet">
<style>
:root{
  --orange:#f37122;
  --orange-soft:#eea75a;
  --green:#8cc63f;
  --green-dark:#7ab73a;
  --green-tile:#97d14a;
  --brown:#3f0e04;
  --ink:#222;
  --text:#555;
  --footer:#2b2b2b;
  --white:#fff;
  --teal:#00a990;
}
*{box-sizing:border-box;margin:0;padding:0}
html,body{width:700px;height:1200px;overflow:hidden}
body{position:relative;background:var(--white);font-family:"Lato",sans-serif;color:var(--text)}
.abs{position:absolute}

/* header */
.site-header{left:0;top:0;width:700px;height:80px;background:var(--white);box-shadow:0 2px 6px rgba(0,0,0,.08);z-index:2}
.brand{left:65px;top:20px;display:flex;align-items:center;gap:8px}
.brand-dot{width:30px;height:30px;border-radius:50%;background:var(--green)}
.brand-name{font-family:"Jost",sans-serif;font-weight:500;font-size:15px;color:var(--green-dark);line-height:1.1;width:140px}
.contact-strip{right:62px;top:19px;display:flex;align-items:center;gap:6px;font-size:9px;color:#444}
.round{width:16px;height:16px;border-radius:50%;display:inline-block}
.nav{right:62px;top:48px;display:flex;font-size:8px;color:#333}
.nav a{color:#333;text-decoration:none;padding:4px 6px;line-height:8px}
.nav a.active{background:var(--orange);color:var(--white)}

/* hero */
.hero{left:0;top:80px;width:700px;height:274px;background:radial-gradient(ellipse at center,#fff 55%,#efefef 100%)}
.hero-kicker{left:65px;top:86px;font-family:"Jost",sans-serif;font-size:18px;color:var(--ink)}
.hero-title{left:65px;top:110px;font-family:"Jost",sans-serif;font-weight:600;font-size:20px;color:var(--orange);white-space:nowrap}
.hero-sub{left:65px;top:138px;font-size:10px;font-style:italic;color:#222}
.btn{background:var(--orange);color:var(--white);font-family:"Jost",sans-serif;font-weight:600;display:flex;align-items:center;justify-content:center}
.hero-btn{left:65px;top:164px;width:127px;height:28px;font-size:13px;font-style:italic;border-radius:2px;box-shadow:0 2px 0 #d85c12}
.hero-photo{left:336px;top:74px;width:348px;height:150px;border-radius:45% 45% 35% 35%;background:radial-gradient(ellipse at 40% 55%,#f6a22a 0%,#8bbf3d 40%,#3f7d2a 72%,rgba(255,255,255,0) 100%)}

/* steps band */
.steps{left:0;top:354px;width:700px;height:76px;background:var(--green)}
.step{top:0;width:96px;height:76px;display:flex;flex-direction:column;align-items:center;padding-top:9px;color:var(--white);font-size:9.5px;text-align:center;line-height:1.15}
.step svg{margin-bottom:5px}
.step.dark{background:var(--green-dark)}
.step.tile{background:var(--green-tile)}

/* about */
.about-title{left:65px;top:455px;font-family:"Jost",sans-serif;font-weight:500;font-size:17px;color:var(--ink)}
.about-text{left:65px;width:312px;font-size:7.8px;line-height:12.8px;color:#555}
.about-btn{left:65px;top:648px;width:96px;height:25px;font-size:11.5px;border-radius:2px}
.order-box{left:445px;top:458px;width:190px;height:213px;background:var(--brown);border-radius:2px;padding:10px 16px;color:var(--white)}
.order-box h3{font-family:"Jost",sans-serif;font-weight:600;font-size:13px;line-height:17px;margin-bottom:6px}
.order-box label{display:block;font-size:7.5px;margin-bottom:4px}
.order-box .field{height:18px;background:var(--white);margin-bottom:13px}
.order-btn{width:69px;height:23px;font-size:10px;border-radius:2px;margin-top:-1px}

/* features */
.features{left:0;top:701px;width:700px;height:292px;background:var(--orange-soft)}
.card{top:33px;width:180px;height:227px;background:var(--white);border-radius:2px;text-align:center}
.card-photo{height:110px;width:100%}
.card h4{margin:11px 0 6px;font-family:"Jost",sans-serif;font-weight:500;font-size:11.5px;color:var(--orange);display:flex;align-items:center;justify-content:center;gap:6px}
.card h4::before,.card h4::after{content:"";width:18px;height:1px;background:var(--orange)}
.card p{font-size:8.3px;line-height:14px;color:#333;padding:0 16px}
.card .more{display:block;margin-top:6px;font-size:7.5px;color:var(--orange)}

/* newsletter */
.news-title{left:76px;top:1009px;font-family:"Jost",sans-serif;font-weight:500;font-size:17px;color:#333}
.news-sub{left:76px;top:1031px;font-size:7.5px;color:#333}
.news-form{left:318px;top:1010px;width:303px;height:30px;border:1px solid #ccc;border-radius:2px;display:flex;background:var(--white)}
.news-form span{flex:1;font-size:7.5px;color:#888;padding:10px 12px}
.news-go{width:40px;height:28px;background:var(--orange);display:flex;align-items:center;justify-content:center}

/* footer */
.site-footer{left:0;top:1060px;width:700px;height:140px;background:var(--footer);color:var(--white)}
.foot-h{font-family:"Jost",sans-serif;font-weight:500;font-size:11px}
.foot-rows{font-size:7px;line-height:10.5px}
.foot-rows td{vertical-align:top;padding-right:6px}
.rule{top:14px;width:1px;height:124px;background:#555}
.foot-social{display:flex;gap:6px}
.foot-social .round{width:19px;height:19px;background:var(--white)}
.foot-form{display:flex;height:18px;width:124px}
.foot-form span{flex:1;background:var(--white);color:#222;font-size:6.5px;padding:5px 6px}
.foot-form b{width:20px;background:#111;font-size:8px;font-weight:400;display:flex;align-items:center;justify-content:center}
.foot-mark{left:485px;top:22px;width:131px;height:62px;border:2px solid #999;border-radius:50%;display:flex;align-items:center;justify-content:center;text-align:center;font-family:"Jost",sans-serif;font-size:11px;color:#aaa;padding:0 12px;line-height:1.2}
.copy{left:490px;top:97px;font-size:7px}
</style>
</head>
<body>

<header class="abs site-header">
  <div class="abs brand"><span class="brand-dot"></span><span class="brand-name">Bright Leaf Bistro &amp; Pantry</span></div>
  <div class="abs contact-strip">
    <span class="round" style="background:#4fb9a6"></span>
    <span style="margin-right:10px">hello@brightleafpantry.com</span>
    <span class="round" style="background:#3b5998"></span>
    <span class="round" style="background:#1da1f2"></span>
    <span class="round" style="background:#4fb9a6"></span>
    <span class="round" style="background:#e0523e"></span>
  </div>
  <nav class="abs nav">
    <a class="active">HOME</a><a>EVENTS</a><a>CAFE</a><a>PRODUCTS</a><a>HEALTH INFO</a><a>NEWS</a><a>RECIPES</a><a>CONTACT US</a>
  </nav>
</header>

<section class="abs hero">
  <div class="abs hero-kicker">WELCOME TO BRIGHT LEAF</div>
  <div class="abs hero-title">NATURAL HEALTHY MEALS</div>
  <div class="abs hero-sub">Delivering&nbsp; Harlow Street, Riverbend and Cedar Vale.</div>
  <div class="abs btn hero-btn">ORDER NOW</div>
  <div class="abs hero-photo" role="img" aria-label="Heap of fresh vegetables and fruit: lettuce, peppers, oranges, tomatoes, cucumbers, grapes"></div>
</section>

<section class="abs steps">
  <div class="abs step dark" style="left:53px"></div>
  <div class="abs step tile" style="left:149px">
    <svg width="42" height="40" viewBox="0 0 42 40" fill="none" stroke="#fff" stroke-width="2.5"><circle cx="18" cy="21" r="16"/><path d="M32 4c-5 0-8 3-8 7 0 5 8 12 8 12s8-7 8-12c0-4-3-7-8-7z" fill="#fff" stroke="none"/><circle cx="32" cy="11" r="3" fill="#97d14a" stroke="none"/></svg>
    Your Location
  </div>
  <div class="abs step tile" style="left:245px">
    <svg width="30" height="40" viewBox="0 0 30 40" fill="#fff"><rect x="6" y="2" width="3" height="16"/><rect x="11" y="0" width="3" height="18"/><rect x="16" y="3" width="3" height="15"/><rect x="21" y="1" width="3" height="17"/><path d="M3 16h24l-3 24H6z"/></svg>
    Choose Takeaway
  </div>
  <div class="abs step tile" style="left:341px">
    <svg width="40" height="40" viewBox="0 0 40 40" fill="#fff"><path d="M8 10l18-8 4 8z"/><rect x="2" y="10" width="34" height="28" rx="5"/><rect x="24" y="20" width="14" height="9" rx="2" fill="#97d14a"/><circle cx="29" cy="24.5" r="2" fill="#fff"/></svg>
    Pay cash or by<br>card
  </div>
  <div class="abs step tile" style="left:437px">
    <svg width="40" height="40" viewBox="0 0 40 40" stroke="#fff" stroke-width="3.5" stroke-linecap="round" fill="none"><path d="M6 36L30 10"/><ellipse cx="31" cy="8" rx="5" ry="7" transform="rotate(45 31 8)" fill="#fff"/><path d="M34 36L12 14"/><path d="M12 14L4 6M12 14l-4-10M12 14l-10-4" stroke-width="2"/></svg>
    Eat &amp; Enjoy
  </div>
  <div class="abs step dark" style="left:533px"></div>
</section>

<section>
  <h2 class="abs about-title">About Us</h2>
  <p class="abs about-text" style="top:490px">Sed ut perspiciatis unde omnis iste natus error sit voluptatem accusantium doloremque laudantium, totam rem aperiam, eaque ipsa quae ab illo inventore veritatis et quasi architecto beatae vitae dicta sunt explicabo. Nemo enim ipsam voluptatem quia volupta s sit aspernatur aut odit aut fugit, sed quia consequuntur magni dolores eos qui ratione voluptatem sequi nesciunt. Neque porro quisquam est, qui dolorem ipsum quia dolor sit amet, consectetur,</p>
  <p class="abs about-text" style="top:580px">adipisci velit, sed quia non numquam eius modi tempora incidunt ut labore et dolore magnam aliquam quaerat voluptatem. Ut enim ad minima veniam, quis nostrum exercitationem ullam corporis suscipit laboriosam, nisi ut aliquid ex ea commodi consequatur Quis autem vel eum iure reprehenderit...</p>
  <div class="abs btn about-btn">LEARN MORE</div>

  <form class="abs order-box">
    <h3>Order Now Your Favorite Food in just Minutes</h3>
    <label>Choose City:</label><div class="field"></div>
    <label>Choose Area:</label><div class="field"></div>
    <label>What do you want to eat</label><div class="field"></div>
    <div class="btn order-btn">Order Now</div>
  </form>
</section>

<section class="abs features">
  <article class="abs card" style="left:65px">
    <div class="card-photo" role="img" aria-label="Strawberries growing in raised greenhouse rows" style="background:linear-gradient(160deg,#3d6b2a,#8fae6a 50%,#c9c3b5)"></div>
    <h4>Locally Grown Produce</h4>
    <p>Lorem ipsum dolor sit amet, consectetur adipiscing elit, sed do eiusmod tempor incididunt ut labore et dolore magna aliqua.</p>
    <span class="more">Read More &gt;&gt;</span>
  </article>
  <article class="abs card" style="left:261px">
    <div class="card-photo" role="img" aria-label="Market stall of vegetables: greens, carrots and red peppers" style="background:linear-gradient(180deg,#c9a43a,#4f8c2e 45%,#d2472a 80%,#e07a2a)"></div>
    <h4>Preservative Groceries</h4>
    <p>Lorem ipsum dolor sit amet, consectetur adipiscing elit, sed do eiusmod tempor incididunt ut labore et dolore magna aliqua.</p>
    <span class="more">Read More &gt;&gt;</span>
  </article>
  <article class="abs card" style="left:457px">
    <div class="card-photo" role="img" aria-label="Natural body care creams in jars on a wooden table with leaves" style="background:linear-gradient(160deg,#5a3d26,#8a6a4a 45%,#e8e2c8 75%,#f3e4a0)"></div>
    <h4>Cruelty-Free Body Care</h4>
    <p>Lorem ipsum dolor sit amet, consectetur adipiscing elit, sed do eiusmod tempor incididunt ut labore et dolore magna aliqua.</p>
    <span class="more">Read More &gt;&gt;</span>
  </article>
</section>

<section>
  <h2 class="abs news-title">Sign Up With Newsletter</h2>
  <p class="abs news-sub">Lorem ipsum Sit amet consectetur adipistion</p>
  <div class="abs news-form">
    <span>Enter Email To Join Our Newsletter</span>
    <div class="news-go"><svg width="18" height="14" viewBox="0 0 18 14" fill="#fff"><path d="M0 4h9V0l9 7-9 7v-4H0z"/></svg></div>
  </div>
</section>

<footer class="abs site-footer">
  <div class="abs" style="left:86px;top:20px">
    <div class="foot-h">CONTACT US</div>
    <table class="foot-rows" style="margin-top:4px;border-collapse:collapse">
      <tr><td>Phone</td><td>:</td><td>+00 (07) 555 2140</td></tr>
      <tr><td>Email</td><td>:</td><td>orders@brightleafpantry.com</td></tr>
      <tr><td>Address</td><td>:</td><td>Unit 4, 210 Harlow Street<br>Harlow Street Market Row<br>Riverbend</td></tr>
    </table>
  </div>
  <div class="abs rule" style="left:268px"></div>
  <div class="abs" style="left:292px;top:20px">
    <div class="foot-h">GET IN TOUCH</div>
    <div class="foot-social" style="margin-top:8px"><span class="round"></span><span class="round"></span><span class="round"></span><span class="round"></span></div>
    <div style="font-size:8px;margin:12px 0 6px">Subscribe monthly Newsletter</div>
    <div class="foot-form"><span>Enter your email address</span><b>GO</b></div>
  </div>
  <div class="abs rule" style="left:443px"></div>
  <div class="abs foot-mark">Bright Leaf Bistro &amp; Pantry</div>
  <div class="abs copy">Copyright © 2015 . All rights Reserved</div>
</footer>

</body>
</html>
```